LED panel tester - hand-held test tool - simple label required

I have designed a product to test the LED panels of a road-side variable message sign (VMS). I don't expect to sell too many of these but thought it would look professional if it had a proper label.

I need a label designed for this hand-held test equipment. Attached is the positional layout of all the switches and text. I have also included a photo of the product.

A simple Google image search of "hand-held test tool" shows that it doesn't have to be fancy but rather functional.

I would like to put branding on the bottom 1/5th and have the option to interchange the brand if I ever get approached by one of the manufacturers of these signs. Initially it will just have a link to my website (TallowbrookWorks.com.au) right down at the bottom.

```html
<!DOCTYPE html>
<html lang="en">
<head>
<meta charset="utf-8">
<title>VMS Panel Tester Label</title>
<link rel="stylesheet" href="https://fonts.googleapis.com/css2?family=Montserrat:wght@600;700;800&display=swap">
<style>
  :root {
    --page-bg: #ffffff;
    --panel-top: #323035;
    --panel-mid: #1b1b1d;
    --panel-bottom: #2a292d;
    --panel-edge: #8a8a90;
    --text-light: #ffffff;
    --button-fill: #555760;
    --ring-red: #e3202a;
    --ring-green: #13a04a;
    --ring-orange: #ef7418;
    --ring-white: #ffffff;
    --ring-blue: #1f3fd6;
    --ring-neutral: #5a5a60;
    --knob-fill: #2a2a2e;
    --screen-bezel: #2d2d31;
    --screen-edge: #6b6b70;
    --screen-fill: #4b4d56;
    --power-led: #8dc63f;
  }
  html, body {
    margin: 0;
    padding: 0;
    width: 1200px;
    height: 1200px;
    overflow: hidden;
    background: var(--page-bg);
  }
  .label-canvas {
    display: block;
    width: 1200px;
    height: 1200px;
  }
  .label-text {
    font-family: "Montserrat", Arial, sans-serif;
    fill: var(--text-light);
  }
  .product-title { font-weight: 800; font-size: 68px; letter-spacing: -1px; }
  .product-subtitle { font-weight: 700; font-size: 17px; letter-spacing: 1.5px; }
  .control-label { font-weight: 700; font-size: 16.5px; }
  .power-label { font-weight: 700; font-size: 12.5px; }
  .website { font-weight: 700; font-size: 19px; }
</style>
</head>
<body>
<svg class="label-canvas" viewBox="0 0 1200 1200" xmlns="http://www.w3.org/2000/svg">
  <defs>
    <linearGradient id="panelShade" x1="0" y1="0" x2="0" y2="1">
      <stop offset="0" stop-color="var(--panel-top)"/>
      <stop offset="0.55" stop-color="var(--panel-mid)"/>
      <stop offset="1" stop-color="var(--panel-bottom)"/>
    </linearGradient>
  </defs>

  <!-- label body -->
  <rect class="label-panel" x="413" y="167" width="373" height="866"
        fill="url(#panelShade)" stroke="var(--panel-edge)" stroke-width="2"/>

  <!-- heading -->
  <text class="label-text product-title" x="600" y="245" text-anchor="middle">VMS</text>
  <text class="label-text product-subtitle" x="600" y="268" text-anchor="middle">PANEL TESTER</text>

  <!-- colour selection buttons -->
  <g class="button-column" stroke-width="3">
    <circle cx="600" cy="327" r="21" fill="var(--button-fill)" stroke="var(--ring-red)"/>
    <circle cx="600" cy="385" r="21" fill="var(--button-fill)" stroke="var(--ring-green)"/>
    <circle cx="600" cy="442" r="21" fill="var(--button-fill)" stroke="var(--ring-orange)"/>
    <circle cx="600" cy="500" r="21" fill="var(--button-fill)" stroke="var(--ring-white)"/>
    <circle cx="600" cy="557" r="21" fill="var(--button-fill)" stroke="var(--ring-blue)"/>
    <circle cx="600" cy="615" r="21" fill="var(--knob-fill)" stroke="var(--ring-neutral)"/>
  </g>
  <g class="label-text control-label">
    <text x="636" y="333">RED</text>
    <text x="632" y="391">GREEN</text>
    <text x="632" y="448">ORANGE</text>
    <text x="632" y="506">WHITE</text>
    <text x="632" y="563">BLUE</text>
    <text x="632" y="621">SLOW</text>
    <text x="568" y="621" text-anchor="end">FAST</text>
  </g>

  <!-- display window -->
  <rect class="screen-bezel" x="520" y="687" width="160" height="115"
        fill="var(--screen-bezel)" stroke="var(--screen-edge)" stroke-width="2"/>
  <rect class="screen-window" x="528" y="697" width="145" height="96" fill="var(--screen-fill)"/>

  <!-- power indicator -->
  <circle class="power-led" cx="721" cy="702" r="10" fill="var(--power-led)"/>
  <text class="label-text power-label" x="722" y="733" text-anchor="middle">POWER</text>

  <!-- branding -->
  <text class="label-text website" x="600" y="997" text-anchor="middle">www.TallowbrookWorks.com.au</text>
</svg>
</body>
</html>
```